Business card design needed

We do excavation, cartage and contracting
I would quote like to have a picture of my digger as the whole back ground and the words on top. If that looks any good
Otherwise please feel free to come up with any other cool options

Cheers Marc

KLR Contracting
Excavation, Cartage, Contracting
Marcus Prewitt
www.klr-example.co.nz
021 584 067
marc@klr-example.co.nz

```html
<!DOCTYPE html>
<html lang="en">
<head>
<meta charset="utf-8">
<title>KLR Contracting – Business Card</title>
<link rel="stylesheet" href="https://fonts.googleapis.com/css2?family=Fira+Sans:wght@300&display=swap">
<style>
  :root {
    --backdrop: #141414;
    --card-green-light: #2f6e3d;
    --card-green-dark: #1d4a28;
    --rule-tint: rgba(255, 255, 255, 0.12);
    --ink: #eef3ee;
  }
  * { margin: 0; padding: 0; box-sizing: border-box; }
  html, body {
    width: 1200px;
    height: 830px;
    overflow: hidden;
    background: var(--backdrop);
  }
  .canvas {
    position: relative;
    width: 1200px;
    height: 830px;
  }
  .business-card {
    position: absolute;
    left: 173px;
    top: 173px;
    width: 856px;
    height: 463px;
    background: radial-gradient(ellipse at 40% 25%, var(--card-green-light), var(--card-green-dark) 85%);
    font-family: "Fira Sans", sans-serif;
    font-weight: 300;
    color: var(--ink);
    overflow: hidden;
  }
  .card-rule {
    position: absolute;
    left: 0;
    right: 0;
    height: 0;
    border-top: 3px solid var(--rule-tint);
  }
  .card-rule--top { top: 38px; }
  .card-rule--bottom { bottom: 38px; }
  .brand-name {
    position: absolute;
    left: 0;
    right: 0;
    top: 100px;
    text-align: center;
    font-size: 96px;
    line-height: 1;
    letter-spacing: 4px;
  }
  .details {
    position: absolute;
    top: 317px;
    list-style: none;
    font-size: 23px;
    line-height: 36.5px;
  }
  .details--services { left: 85px; }
  .details--contact { left: 572px; }
</style>
</head>
<body>
<div class="canvas">
  <section class="business-card">
    <div class="card-rule card-rule--top"></div>
    <div class="card-rule card-rule--bottom"></div>

    <h1 class="brand-name">KLR</h1>

    <ul class="details details--services">
      <li>KLR Contracting Excavation</li>
      <li>Cartage</li>
      <li>Contracting Marcus Prewitt</li>
    </ul>

    <ul class="details details--contact">
      <li>www.klr-example.co.nz</li>
      <li>021 584 067</li>
      <li>marc@klr-example.co.nz</li>
    </ul>
  </section>
</div>
</body>
</html>
```